Worknest Background Picture

Professional WorkNest Banner Design for Individual in Architectural Industry

Hello talented designers,

I am looking for a creative and professional graphic designer to create a WorkNest banner for my personal profile. I am deeply involved in the architectural systems industry, specializing in innovative and sustainable building solutions.

What I'm Looking For:

Personal Branding: The banner should reflect my professional identity and role in the architectural systems industry. It should be more personal than corporate.

Visual Elements: Include imagery or abstract designs that represent architecture, innovation, and sustainability. The design should subtly hint at my industry expertise and areas of specialization.

Professional and Engaging: The design should be visually striking but maintain a professional look. It should engage viewers and encourage them to learn more about my professional background and skills.

File Requirements: The final design should be provided in a high-resolution JPEG or PNG format, fitting WorkNest's banner dimensions.

To Apply, Please Provide:

A summary of your design experience, especially with WorkNest banners or personal branding projects.
A portfolio showcasing your previous work, highlighting any designs related to personal branding or professional themes.
Your estimated timeline and budget for the project.
Selection Criteria:

Creativity in reflecting a personal professional brand.
Experience with individual professional branding.
Quality and relevance of the portfolio.
Competitive pricing and clear communication.
I am excited to see your creative approaches and look forward to collaborating to craft a banner that perfectly encapsulates my professional persona on WorkNest.

Thank you!

My worknest page:
worknest.example/in/morbevatki

Our website:

https://filebox.example/shared/folders/7qTbXwNpLmRzA2sKdHvYc94eoFjUi0BnM?usp=share_link

Some photos of our projects:

```html
<!DOCTYPE html>
<html lang="en">
<head>
<meta charset="UTF-8">
<title>Profile Banner – Architecture, Innovation &amp; Sustainability</title>
<link rel="stylesheet" href="https://fonts.googleapis.com/css2?family=EB+Garamond:wght@400&display=swap">
<style>
  :root {
    --canvas-bg: #f3f3f3;
    --banner-white: #ffffff;
    --slate-band: #6b7f9a;
    --mist-panel: #c9d2df;
    --ink: #141414;
    --room-light: #d6d2c6;
    --room-floor: #9a7b57;
    --sky-top: #5b8fd6;
    --facade-blue: #2d4470;
  }
  html, body {
    margin: 0;
    padding: 0;
    width: 1200px;
    height: 1200px;
    overflow: hidden;
    background: var(--canvas-bg);
  }
  .stage {
    width: 1200px;
    height: 1200px;
    display: flex;
    align-items: center;
    justify-content: center;
  }
  .profile-banner {
    display: block;
    width: 989px;
    height: 246px;
    background: var(--banner-white);
  }
  .banner-tagline {
    font-family: "EB Garamond", Georgia, serif;
    font-size: 30px;
    fill: var(--ink);
  }
</style>
</head>
<body>
  <main class="stage">
    <svg class="profile-banner" viewBox="0 0 790 197" xmlns="http://www.w3.org/2000/svg">
      <defs>
        <linearGradient id="room-tones" x1="0" y1="0" x2="0" y2="1">
          <stop offset="0" stop-color="#dfe3e6"/>
          <stop offset="0.6" stop-color="var(--room-light)"/>
          <stop offset="1" stop-color="var(--room-floor)"/>
        </linearGradient>
        <linearGradient id="building-tones" x1="0" y1="0" x2="0" y2="1">
          <stop offset="0" stop-color="var(--sky-top)"/>
          <stop offset="0.55" stop-color="#4a6fa8"/>
          <stop offset="1" stop-color="var(--facade-blue)"/>
        </linearGradient>
      </defs>

      <rect class="banner-base" x="0" y="0" width="790" height="197" fill="var(--banner-white)"/>

      <polygon class="slate-band" points="0,0 110,0 162,197 104,197" fill="var(--slate-band)"/>

      <polygon class="interior-photo" role="img" aria-label="Photo of a bright empty apartment interior with large windows and wood floor"
               points="170,0 380,0 280,197 125,197" fill="url(#room-tones)"/>

      <polygon class="mist-panel" points="254,0 549,0 620,197 359,197" fill="var(--mist-panel)" opacity="0.82"/>

      <polygon class="building-photo" role="img" aria-label="Photo of a modern mid-rise residential building with balconies under a blue sky"
               points="634,0 790,0 790,197 529,197" fill="url(#building-tones)"/>

      <g class="banner-tagline">
        <text x="424" y="62">Architecture</text>
        <text x="379" y="107">Innovation &amp;</text>
        <text x="347" y="150">Sustainability</text>
      </g>
    </svg>
  </main>
</body>
</html>
```